MU LI TAO Chocolate Bar

Create new, modifyable 2D image from existing non-modifyable JPEG image of chocolate bar packaging. For China market. Must be able to at least work with or know how to modify Chinese characters, very simple, just a few, you don't need to understand what they mean, but may require changing font/colouring of characters I supply.

1) Create new, modifyable 2D image from existing non-modifyable JPEG image of chocolate bar packaging (in reality bar packaging will be 17cm in length, 3.8cm in width, and 1.4cm in height). Keep existing color scheme for background and all fonts.

2) Replace "ZUMPA" with the Chinese characters "木里桃” in the same colour. Delete the blue words beneath "Caffeinated Chocolate/Chocolat Cafeine". Extend the new yellow lettering "木里桃” downwards to cover the whole area including the area where the blue words used to be.

3) Delete the orange lettering "CHO-CO-LATE" to the right of the "ZUMPA" lettering. In this new blank void, you will place two new Chinese words, each 3 characters in length, aligned vertically, parallel to one another. The first word (3 characters) is ”咖啡因“。This word should stretch from the top border, starting with 咖,then 啡 in the middle directly below,then 因 at the bottom. This three character word should be in the same blue colour as the "Caffeinated Chocolate.." words that you deleted in step 2. THEN, diretly to the right of this 3 character, vertically aligned word 咖啡因,is the second 3 character, vertically aligned word: “巧克力”。巧 is the character on top, 克 is the character in the middle, and 力 is the character on the bottom. This 3 character word 巧克力 should be in the same orange colour as the word "CHO-CO-LATE" that you deleted earlier.
Updates

Updated brief, included pictures, detailed description, and simplified requirements. Added Monday, January 19, 2015

Simplified and updated brief. Create 2D modifyable image from non-modifyable JPEG original image of chocolate bar packaging. Changing lettering only, not changing logo. Should be much simpler this way. Added Monday, January 19, 2015

Target Market(s)

China, consumers, on-shelf, consumer packaged good

Industry/Entity Type

Work

Logo Text

木里桃:咖啡因巧克力。柏诺维:功能食品。

Logo styles of interest
Character Logo
Font styles to use
Serif

Requirements
Must have
• Same as in project description.
Nice to have
• If you can supply in modifyable 3D version as well, that would be great. The 2 sides and back don't need any labeling at this point, but would help a lot for next steps. Nice to have.

```html
<!DOCTYPE html>
<html lang="zh-CN">
<head>
<meta charset="utf-8">
<title>木里桃 咖啡因巧克力 包装</title>
<link rel="stylesheet" href="https://fonts.googleapis.com/css2?family=Noto+Sans+SC:wght@400;500&display=swap">
<style>
  :root {
    --stage: #7a4e2a;
    --wrapper-top: #5c3b29;
    --wrapper-mid: #3a2216;
    --wrapper-bottom: #120a06;
    --title-yellow: #f8d700;
    --caffeine-blue: #5cc2dc;
    --choco-orange: #f0922a;
    --owl-orange: #e98a2c;
    --owl-blue: #3bb6d0;
  }
  * { margin: 0; padding: 0; box-sizing: border-box; }
  html, body { width: 1200px; height: 1000px; overflow: hidden; }
  body {
    background: var(--stage);
    font-family: "Noto Sans SC", sans-serif;
    position: relative;
  }
  .wrapper {
    position: absolute;
    left: 0; top: 322px;
    width: 1200px; height: 354px;
    background: linear-gradient(180deg, var(--wrapper-top) 0%, var(--wrapper-mid) 45%, var(--wrapper-bottom) 100%);
  }
  .brand-title {
    position: absolute;
    left: 34px; top: 40px;
    font-size: 212px;
    font-weight: 400;
    line-height: 1;
    letter-spacing: 4px;
    color: var(--title-yellow);
    white-space: nowrap;
  }
  .descriptor {
    position: absolute;
    top: 52px;
    display: flex;
    flex-direction: column;
    font-size: 72px;
    line-height: 84px;
    font-weight: 400;
  }
  .descriptor--caffeine { left: 718px; top: 58px; color: var(--caffeine-blue); }
  .descriptor--chocolate { left: 806px; top: 38px; color: var(--choco-orange); }
  .mascot {
    position: absolute;
    left: 922px; top: 22px;
    width: 190px; height: 308px;
  }
  .maker-line {
    position: absolute;
    left: 1146px; top: 310px;
    transform-origin: left top;
    transform: rotate(-90deg);
    font-size: 31px;
    font-weight: 400;
    letter-spacing: 1px;
    color: var(--choco-orange);
    white-space: nowrap;
  }
</style>
</head>
<body>
  <section class="wrapper">
    <h1 class="brand-title">木里桃</h1>
    <div class="descriptor descriptor--caffeine"><span>咖</span><span>啡</span><span>因</span></div>
    <div class="descriptor descriptor--chocolate"><span>巧</span><span>克</span><span>力</span></div>
    <svg class="mascot" viewBox="0 0 190 308" role="img" aria-label="Illustration of an orange owl mascot with a blue scaled wing">
      <defs>
        <linearGradient id="mascot-fill" x1="0" y1="0" x2="0" y2="1">
          <stop offset="0" stop-color="var(--owl-orange)"/>
          <stop offset="1" stop-color="var(--owl-blue)"/>
        </linearGradient>
      </defs>
      <rect x="4" y="4" width="182" height="296" rx="40" fill="url(#mascot-fill)" opacity="0.55"/>
    </svg>
    <p class="maker-line">柏诺维 功能食品</p>
  </section>
</body>
</html>
```